Pathways to Brightmoor Land Ventures

size of the ad - 8”x 10.75" plus 0.25" bleed
I would like an ad for a magazine that will stand out and make people want to read the ad.
The ad should not be crowded and people reading the ad will be able to read the text.
I would like it to be a creative and modern-day design.
the list of topics should not be the focus of the ad.
the text is attached.
If you decide to use people in the ad then please no ladies.
please note that leave over 1 inch for the bottom of the footer

```html
<!DOCTYPE html>
<html lang="en">
<head>
<meta charset="utf-8">
<title>Real Estate Course</title>
<link href="https://fonts.googleapis.com/css2?family=Bebas+Neue&family=Poppins:wght@400;500;600&display=swap" rel="stylesheet">
<style>
  :root {
    --navy: #13306b;
    --red: #e02a43;
    --ink: #111318;
    --paper: #ffffff;
    --backdrop: #2a323b;
    --rule: #b9bcc4;
  }
  * { margin: 0; padding: 0; box-sizing: border-box; }
  html, body { width: 1200px; height: 2736px; overflow: hidden; }
  body { background: var(--backdrop); font-family: "Poppins", sans-serif; color: var(--ink); position: relative; }

  .flyer {
    position: absolute; left: 50px; top: 659px;
    width: 1100px; height: 1418px;
    background: var(--paper); overflow: hidden;
  }
  .hero-photo {
    position: absolute; right: 0; top: 0; width: 520px; height: 900px;
    background:
      radial-gradient(ellipse at 62% 42%, #8f8378 0%, #b9ada0 22%, #e6e1da 45%, rgba(255,255,255,0) 70%),
      linear-gradient(180deg, #f4f2ef 0%, #ffffff 100%);
  }
  .headline {
    position: absolute; left: 118px; top: 108px;
    font-family: "Bebas Neue", sans-serif; font-size: 132px; line-height: 0.84; letter-spacing: 1px;
  }
  .headline .line-navy { color: var(--navy); display: block; }
  .headline .line-red { color: var(--red); display: block; }
  .program-title {
    position: absolute; left: 116px; top: 368px; width: 560px;
    font-size: 52px; font-weight: 400; line-height: 64px; text-transform: uppercase;
  }
  .tagline {
    position: absolute; left: 116px; top: 580px; width: 520px;
    font-size: 44px; font-weight: 400; line-height: 48px;
  }
  .session-badge {
    position: absolute; left: 120px; top: 754px; width: 328px; height: 328px;
    border-radius: 50%; background: var(--red); color: var(--paper);
    display: flex; flex-direction: column; align-items: center; justify-content: center; text-align: center;
  }
  .session-badge::after {
    content: ""; position: absolute; inset: 16px; border: 2px solid rgba(255,255,255,0.85); border-radius: 50%;
  }
  .session-badge .place { font-size: 44px; line-height: 46px; }
  .session-badge .detail { font-size: 22px; line-height: 22px; margin-top: 4px; }
  .session-badge .gap { margin-top: 18px; }
  .early-bird {
    position: absolute; left: 149px; top: 1090px; width: 300px;
    font-size: 18px; font-weight: 500; line-height: 21px;
  }
  .early-bird p + p { margin-top: 16px; }
  .topics {
    position: absolute; left: 487px; top: 758px;
  }
  .topics h2 { font-size: 44px; font-weight: 400; line-height: 44px; }
  .topic-columns { display: flex; gap: 36px; margin-top: 30px; }
  .topic-list { list-style: none; width: 228px; }
  .topic-list li {
    position: relative; padding: 4px 0 8px 14px; margin-bottom: 8px;
    font-size: 18px; font-weight: 600; line-height: 21px;
    border-bottom: 2px dashed var(--rule);
  }
  .topic-list li::before {
    content: ""; position: absolute; left: 0; top: 11px; width: 7px; height: 7px; border-radius: 50%; background: var(--red);
  }
  .footer-waves { position: absolute; left: 0; bottom: 0; width: 1100px; height: 240px; }
</style>
</head>
<body>
  <main class="flyer">
    <div class="hero-photo" role="img" aria-label="Photo of a hand holding a model house with stacked coins behind it"></div>

    <h1 class="headline">
      <span class="line-navy">Real Estate</span>
      <span class="line-red">Course</span>
    </h1>

    <p class="program-title">Pathways to Brightmoor Land Ventures</p>

    <p class="tagline">Investing In Knowledge Is Investing In Opportunities</p>

    <div class="session-badge">
      <span class="place">Larkvale</span>
      <span class="detail">10 –Tuesday evenings<br>sessions</span>
      <span class="detail gap">Starting Feb.28</span>
      <span class="detail gap">Limited Partial S<br>cholarships</span>
    </div>

    <div class="early-bird">
      <p>Early Bird Special</p>
      <p>For those that started or would like to go into real estate</p>
    </div>

    <section class="topics">
      <h2>Topics:<br>partial listing</h2>
      <div class="topic-columns">
        <ul class="topic-list">
          <li>Real estate investment strategies</li>
          <li>Due diligence</li>
          <li>Financing</li>
          <li>Underwriting</li>
          <li>Property management</li>
        </ul>
        <ul class="topic-list">
          <li>Real estate Legal basics</li>
          <li>Sourcing deals</li>
          <li>Syndication</li>
          <li>Dealing with brokers</li>
          <li>Tax fundamentals</li>
        </ul>
      </div>
    </section>

    <svg class="footer-waves" viewBox="0 0 1100 240" preserveAspectRatio="none" aria-hidden="true">
      <path fill="var(--navy)" d="M0 90 C40 40 90 20 150 22 C260 26 360 140 493 144 C640 148 760 70 880 30 C960 5 1040 0 1100 10 L1100 240 L0 240 Z"/>
      <path fill="var(--red)" d="M544 240 C640 200 760 150 860 90 C940 45 1010 30 1100 28 L1100 240 Z"/>
    </svg>
  </main>
</body>
</html>
```